Harlow Ironworks Business Card

We need a business card design for a new small metal fabrication business in rural NSW, Australia.

The business (Harlow Ironworks) is owner operated by a man with the initials KB - much of the branding comes from this name.

Harlow Ironworks designs, engineers, repairs and manufactures a range of custom, quality metal works including vehicle trays, agricultural machinery impliments, trailers, wood splitters, fire pits, furniture etc.

The brand position focuses on custom work of the highest quality.

Business card design should show quality, attention to detail and stand out among a mass of business cards.

Logos are in the files

The grey color may be changed on the logo if required to stand out more.

There is an image attached of a simple card that is liked because it is clean, clear, simple, masculine and effective. It says 'quality'. As most of the work we do is custom it would be good to have the business card speak to this.

Target Market(s)

Rural and regional based Australians. Primarily adult male 25-60 yrs. Primary production / rural / travelling lifestyle.

Industry/Entity Type

Metal Fabrication

Contact Information for Business Card

The words 'custom quality fabrications' would be great somewhere perhaps on the backside (not on the information side)
Name
title
Phone: 0418 539 746 and (02) 6193 4827
email: info@harlowiw.com.au
www.harlowiw.com.au

address (2 lines)

Requirements
Nice to have
• Background colour should be very navy blue or black.
Should not have
• NO orange and blue combinations.
• Navy is OK

```html
<!DOCTYPE html>
<html lang="en">
<head>
<meta charset="utf-8">
<title>Harlow Ironworks Business Card</title>
<link rel="stylesheet" href="https://fonts.googleapis.com/css2?family=Questrial&display=swap">
<style>
  :root {
    --stage: #2f2f2f;
    --card: #1c1c1c;
    --card-back: #1a1a1a;
    --green: #6cc04a;
    --grey: #b9b9b9;
    --white: #ececec;
    --muted: #a9a9a9;
    --gear-tone: #262626;
  }
  * { box-sizing: border-box; margin: 0; padding: 0; }
  html, body {
    width: 1200px; height: 516px; overflow: hidden;
    background: var(--stage);
    font-family: "Questrial", "Century Gothic", sans-serif;
  }
  .canvas { position: relative; width: 1200px; height: 516px; }
  .card {
    position: absolute; top: 123px; width: 456px; height: 281px;
    background: var(--card);
    box-shadow: 0 6px 18px rgba(0,0,0,0.45);
    overflow: hidden;
  }
  .card--front { left: 132px; }
  .card--back { left: 600px; background: var(--card-back); }

  .brand { display: flex; align-items: center; gap: 10px; }
  .brand__mark { width: 30px; height: 30px; background: var(--green); flex: none; }
  .brand__name {
    color: var(--grey); font-size: 25px; letter-spacing: 1.5px;
    text-transform: uppercase; line-height: 1;
  }
  .card--front .brand { position: absolute; left: 28px; top: 48px; }

  .gear-field {
    position: absolute; left: 192px; top: 100px; width: 264px; height: 181px;
    background: radial-gradient(ellipse at 55% 55%, var(--gear-tone) 0%, rgba(38,38,38,0.5) 55%, rgba(28,28,28,0) 80%);
  }

  .contact { position: absolute; left: 28px; top: 111px; color: var(--white); }
  .contact__name { color: var(--green); font-size: 14px; line-height: 18px; }
  .contact__title { color: var(--muted); font-size: 10px; line-height: 14px; }
  .contact__address { margin-top: 12px; font-size: 12.5px; line-height: 14px; }
  .contact__list { list-style: none; margin-top: 12px; font-size: 12.5px; line-height: 15.5px; }
  .contact__list li { display: flex; align-items: center; gap: 4px; }
  .contact__list svg { width: 10px; height: 10px; flex: none; }

  .card--back .brand { position: absolute; left: 0; right: 0; top: 116px; justify-content: center; }
  .card--back .brand__mark { width: 36px; height: 36px; }
  .card--back .brand__name { font-size: 30px; }
  .tagline {
    position: absolute; left: 0; right: 0; top: 188px; text-align: center;
    color: var(--green); font-size: 15.5px; letter-spacing: 0.3px;
  }
</style>
</head>
<body>
<main class="canvas">
  <section class="card card--front">
    <div class="gear-field" role="img" aria-label="Faint interlocking gears decoration"></div>
    <div class="brand">
      <span class="brand__mark"></span>
      <span class="brand__name">Harlow Ironworks</span>
    </div>
    <div class="contact">
      <p class="contact__name">Employee Name</p>
      <p class="contact__title">Owner</p>
      <p class="contact__address">88 Workshop Lane,<br>Gundagai, NSW 2722</p>
      <ul class="contact__list">
        <li><svg viewBox="0 0 10 10"><rect x="2.5" y="0.5" width="5" height="9" rx="1" fill="none" stroke="var(--green)" stroke-width="1"/><rect x="4" y="7.5" width="2" height="1" fill="var(--green)"/></svg>0418 539 746</li>
        <li><svg viewBox="0 0 10 10"><rect width="10" height="10" rx="1.5" fill="var(--green)"/><path d="M3 2.2 L4.3 3.6 L3.7 4.4 Q4.5 5.8 5.7 6.4 L6.4 5.7 L7.8 7 L7 8 Q4 7.6 2.2 3 Z" fill="var(--card)"/></svg>(02) 6193 4827</li>
        <li><svg viewBox="0 0 10 10"><rect x="0.5" y="2" width="9" height="6.5" fill="var(--green)"/><path d="M0.5 2 L5 5.6 L9.5 2" fill="none" stroke="var(--card)" stroke-width="0.9"/></svg>info@harlowiw.com.au</li>
        <li><svg viewBox="0 0 10 10"><g fill="none" stroke="var(--green)" stroke-width="0.8"><circle cx="5" cy="5" r="4.4"/><ellipse cx="5" cy="5" rx="2" ry="4.4"/><path d="M0.6 5 H9.4 M1.4 2.8 H8.6 M1.4 7.2 H8.6"/></g></svg>www.harlowiw.com.au</li>
      </ul>
    </div>
  </section>

  <section class="card card--back">
    <div class="brand">
      <span class="brand__mark"></span>
      <span class="brand__name">Harlow Ironworks</span>
    </div>
    <p class="tagline">Custom Quality Fabrications</p>
  </section>
</main>
</body>
</html>
```